R7M Meridian Business Card Design

We need a business card created for our New Business "R7M Meridian"<br/><br/>The business card design is up to you however the following information must be on the business card:<br/><br/>Front of the business card -<br/>Email :dorianv@r7mmeridian.nz<br/>Mobile: +64 (0) 22 4871 659<br/>Website: www.r7mmeridian.nz<br/>Card Owner Name: Dorian Valcourt<br/>Company Title: Business Development Manager<br/>Slogan: "Made well for every occasion". <br/>Logo On the front attached to the design brief<br/><br/>On the back: <br/>Space on the back for 4 more versions of the logo across the bottom of the card indicating different subsidiary brands - R7M Coffee, R7M Arts, R7M ?? (The card will be used for all of these brands - We Will add the extra subsidiary logos to the design once the design is finished (We are a graphics design team). <br/><br/>Other than that we want a premium feeling logo that remains universally usable depending on the business entity that we are using the card for. The use of bright bold colours would be great but we still want the card to feel premium.
Target Market(s)
Gift Design and Manufacturing Companies
Contact Information for Business Card
Front of the business card -
Email :dorianv@r7mmeridian.nz
Mobile: +64 (0) 22 4871 659
Website: www.r7mmeridian.nz
Card Owner Name: Dorian Valcourt
Company Title: Business Development Manager
Slogan: "Made well for every occasion".
Logo On the front attached to the design brief

```html
<!DOCTYPE html>
<html lang="en">
<head>
<meta charset="utf-8">
<title>R7M Meridian Business Card</title>
<link href="https://fonts.googleapis.com/css2?family=Lato:wght@400;700;900&display=swap" rel="stylesheet">
<style>
  :root {
    --brand-blue: #3647a1;
    --ink: #222428;
    --muted: #3a3c40;
    --paper: #ffffff;
    --backdrop: #e9eaec;
  }
  * { box-sizing: border-box; margin: 0; padding: 0; }
  html, body {
    width: 1200px; height: 900px; overflow: hidden;
    background: var(--backdrop);
    font-family: "Lato", sans-serif;
  }
  .stage { position: relative; width: 1200px; height: 900px; }
  .card {
    position: absolute; left: 250px; width: 700px; height: 400px;
    border-radius: 34px;
    box-shadow: 0 6px 18px rgba(0,0,0,0.18);
    overflow: hidden;
  }
  .card--back { top: 30px; background: var(--brand-blue); }
  .card--front { top: 470px; background: var(--paper); }

  /* back side */
  .back-divider {
    position: absolute; left: 349px; top: 110px; width: 1px; height: 180px;
    background: rgba(255,255,255,0.8);
  }
  .sub-brand {
    position: absolute;
    color: var(--paper); font-weight: 700; font-size: 24px; line-height: 30px;
    white-space: nowrap;
  }
  .sub-brand--main   { right: 380px; top: 145px; }
  .sub-brand--plain  { right: 380px; top: 235px; }
  .sub-brand--coffee { left: 380px; top: 120px; }
  .sub-brand--arts   { left: 380px; top: 210px; }

  /* front side */
  .front-logo {
    position: absolute; left: 40px; top: 185px; width: 275px;
    color: var(--brand-blue); font-weight: 900; font-size: 34px; line-height: 40px;
    white-space: nowrap; text-align: center;
  }
  .front-divider {
    position: absolute; left: 335px; top: 95px; width: 2px; height: 190px;
    background: var(--brand-blue);
  }
  .holder { position: absolute; left: 365px; top: 78px; }
  .holder__name {
    color: var(--brand-blue); font-weight: 900; font-size: 31px; line-height: 1.1;
  }
  .holder__title { color: var(--muted); font-size: 17px; margin-top: 4px; }
  .contacts { position: absolute; left: 365px; top: 170px; list-style: none; }
  .contacts li {
    display: flex; align-items: center; gap: 12px;
    color: var(--ink); font-size: 16px; height: 32px;
  }
  .contacts svg { width: 18px; height: 18px; flex: none; }
  .slogan {
    position: absolute; left: 395px; top: 330px;
    color: var(--ink); font-size: 18px;
  }
</style>
</head>
<body>
<main class="stage">
  <section class="card card--back" aria-label="Business card back">
    <div class="sub-brand sub-brand--main">R7M Meridian</div>
    <div class="sub-brand sub-brand--plain">R7M</div>
    <div class="back-divider"></div>
    <div class="sub-brand sub-brand--coffee">R7M Coffee</div>
    <div class="sub-brand sub-brand--arts">R7M Arts</div>
  </section>

  <section class="card card--front" aria-label="Business card front">
    <div class="front-logo">R7M Meridian</div>
    <div class="front-divider"></div>
    <div class="holder">
      <h1 class="holder__name">Dorian Valcourt</h1>
      <p class="holder__title">Business Development Manager</p>
    </div>
    <ul class="contacts">
      <li>
        <svg viewBox="0 0 24 24" aria-hidden="true"><path fill="#3647a1" d="M6.6 10.8a15.1 15.1 0 0 0 6.6 6.6l2.2-2.2c.3-.3.7-.4 1-.2 1.1.4 2.3.6 3.6.6.6 0 1 .4 1 1V20c0 .6-.4 1-1 1C10.6 21 3 13.4 3 4c0-.6.4-1 1-1h3.5c.6 0 1 .4 1 1 0 1.3.2 2.5.6 3.6.1.3 0 .7-.2 1z"/></svg>
        +64 (0) 22 4871 659
      </li>
      <li>
        <svg viewBox="0 0 24 24" aria-hidden="true"><rect x="2" y="5" width="20" height="14" rx="1.5" fill="#3647a1"/><path d="M3 6l9 7 9-7" fill="none" stroke="#fff" stroke-width="1.6"/></svg>
        dorianv@r7mmeridian.nz
      </li>
      <li>
        <svg viewBox="0 0 24 24" aria-hidden="true"><circle cx="12" cy="12" r="9" fill="none" stroke="#3647a1" stroke-width="2"/><ellipse cx="12" cy="12" rx="4" ry="9" fill="none" stroke="#3647a1" stroke-width="1.5"/><path d="M3 12h18M5 7.5h14M5 16.5h14" stroke="#3647a1" stroke-width="1.3"/></svg>
        www.r7mmeridian.nz
      </li>
    </ul>
    <p class="slogan">Made well for every occasion</p>
  </section>
</main>
</body>
</html>
```